Brightvale Cherries Rainier POS Card 7"H x 11"W

We are wanting to create a one-sided 7 x 11 Rainier cherry card that is eye catching and informative.This should be clear and easy to read and not cluttered. We use these cards as a display in grocery stores, demo stands, and other events to market Brightvale Rainier Cherries. We have a few facts that we would like displayed on the card (see below).

Target Market(s)

Consumers

Industry/Entity Type

Agriculture

Font styles to use
Sans Serif

Requirements
Must have
• Yellow cherries - yellow fruit (the blush on the skin is a kiss from the sun)
• Juice doesn't stain - Kid Friendly
• Add contrast to your summer table
• Sweetest Variety - still low glycemic
• Source of Vitamin C, Source of Potassium, and Source of Melatonin
• Rainiers take up to 4x as much work as red cherries
• Natural Color palettes
• Easy to read
• Brightvale Cherries
Nice to have
• Unique, creative, realistc Rainier cherry designs
Should not have
• pastel or neon color scheme, overly cutesy elements

```html
<!DOCTYPE html>
<html lang="en">
<head>
<meta charset="utf-8">
<title>Brightvale Cherries – Yellow Cherries POS Card</title>
<link href="https://fonts.googleapis.com/css2?family=Fira+Sans:ital,wght@0,400;0,600;0,700;1,400;1,500&family=Fira+Sans+Condensed:ital,wght@1,800&family=Great+Vibes&family=Cormorant+Garamond:ital,wght@1,500&display=swap" rel="stylesheet">
<style>
  :root {
    --frame: #000;
    --sun-light: #fde870;
    --sun: #f8d51c;
    --sun-deep: #f2c200;
    --maroon: #7c1a3c;
    --orange: #f39a1c;
    --brown: #6b3d12;
    --ink: #2b1d14;
    --white: #ffffff;
    --fruit-light: #ffd84a;
    --fruit-deep: #f0a21a;
  }
  html, body { margin: 0; padding: 0; overflow: hidden; background: var(--white); }
  .card {
    position: relative; width: 1200px; height: 773px;
    background: var(--frame); overflow: hidden;
    font-family: "Fira Sans", sans-serif;
  }
  .panel {
    position: absolute; inset: 13px; overflow: hidden;
    background: radial-gradient(ellipse at 30% 40%, var(--sun-light) 0%, var(--sun) 55%, var(--sun-deep) 100%);
  }
  .brand {
    position: absolute; left: 44px; top: 58px;
    display: flex; align-items: center; gap: 14px;
  }
  .brand-dot { width: 44px; height: 44px; border-radius: 50%; background: var(--maroon); }
  .brand-name { font-size: 40px; font-weight: 600; color: var(--ink); }
  .title {
    position: absolute; right: 40px; top: 28px; margin: 0;
    font-family: "Great Vibes", cursive; font-weight: 400;
    font-size: 112px; line-height: 1; color: var(--white);
    text-shadow: 0 0 2px #7a5a10, 2px 3px 4px rgba(90,60,0,.45);
  }
  .tagline {
    position: absolute; right: 48px; top: 180px; margin: 0;
    font-family: "Cormorant Garamond", serif; font-style: italic; font-weight: 500;
    font-size: 20px; color: var(--ink);
  }
  .fruit-photo {
    position: absolute; left: 22px; top: 200px; width: 640px; height: 480px;
    border-radius: 46% 46% 40% 40%;
    background: radial-gradient(ellipse at 45% 55%, var(--fruit-light) 0%, var(--fruit-deep) 80%, rgba(240,162,26,0) 100%);
  }
  .band {
    position: absolute; left: 33px; top: 683px; width: 760px; height: 44px;
    border-radius: 22px 0 0 22px; background: var(--maroon);
    color: var(--white); font-size: 22px; line-height: 44px;
    padding-left: 14px; box-sizing: border-box; letter-spacing: .2px;
  }
  .bubble {
    position: absolute; border-radius: 50%; background: radial-gradient(circle at 40% 35%, #fff 60%, #e9e9e9 100%);
    box-shadow: 0 4px 14px rgba(90,60,0,.35);
  }
  .bubble-large { left: 691px; top: 300px; width: 660px; height: 660px; }
  .bubble-small {
    left: 627px; top: 227px; width: 220px; height: 220px;
    display: flex; align-items: center; justify-content: center; text-align: center;
  }
  .nutrition {
    margin: 0; font-style: italic; font-weight: 500; font-size: 22px; line-height: 32px;
    color: var(--brown); width: 180px;
  }
  .benefits { position: absolute; right: 55px; top: 358px; text-align: right; }
  .benefit-hero {
    margin: 0; font-family: "Fira Sans Condensed", sans-serif; font-style: italic; font-weight: 800;
    line-height: 1; color: var(--maroon);
  }
  .hero-juice { font-size: 66px; }
  .hero-stain { font-size: 56px; margin-top: 2px; }
  .hero-kid { font-size: 58px; color: var(--orange); margin-top: 2px; }
  .contrast { margin: 36px 0 0; font-style: italic; font-size: 26px; color: var(--ink); }
  .sweet { margin: 18px 0 0; font-weight: 700; font-size: 34px; color: var(--brown); }
  .glycemic { margin: 4px 0 0; font-size: 25px; color: var(--brown); }
</style>
</head>
<body>
<div class="card">
  <div class="panel">
    <div class="fruit-photo" role="img" aria-label="Photo of three ripe yellow Rainier cherries with green leaves"></div>

    <div class="brand">
      <span class="brand-dot"></span>
      <span class="brand-name">Brightvale Cherries</span>
    </div>

    <h1 class="title">Yellow Cherries</h1>
    <p class="tagline">yellow fruit (the blush on the skin is a kiss from the sun)</p>

    <div class="band">RAINIERS TAKE UP TO 4X AS MUCH WORK AS RED CHERRIES</div>

    <div class="bubble bubble-large"></div>
    <div class="bubble bubble-small">
      <p class="nutrition">Source of Vitamin C, Source of Potassium, and Source of Melatonin</p>
    </div>

    <div class="benefits">
      <p class="benefit-hero hero-juice">Juice</p>
      <p class="benefit-hero hero-stain">doesn't stain</p>
      <p class="benefit-hero hero-kid">Kid Friendly</p>
      <p class="contrast">Add contrast to your summer table</p>
      <p class="sweet">Sweetest Variety</p>
      <p class="glycemic">- Still low glycemic</p>
    </div>
  </div>
</div>
</body>
</html>
```